Flooring Company Wordpress Design Using Elementor

We need a website design using elementor for a flooring company. I have attached a word document with the entire content for the site. I have sample websites www.pellmarbuildersnevada.com and www.tilbrookfinishesreno.com

The site needs to look alot better than the samples. Modern and professional is what we are looking for. 100 times better than the sample websites.

I have images to be used in the site but the file is to large to attached here.

```html
<!DOCTYPE html>
<html lang="en">
<head>
<meta charset="utf-8">
<title>Keystone Flooring Florida</title>
<link rel="stylesheet" href="https://fonts.googleapis.com/css2?family=Arimo:ital,wght@0,400;0,700;1,400&display=swap">
<style>
:root{
  --yellow:#ffd200;
  --blue:#1858a8;
  --blue-deep:#0f4c9c;
  --nav:#454545;
  --ink:#222;
  --muted:#777;
  --grey-bg:#ececec;
  --btn-grey:#c4c4c4;
  --field:#ececec;
}
*{box-sizing:border-box;margin:0;padding:0}
html,body{width:1200px;height:3861px;overflow:hidden}
body{font-family:Arimo,sans-serif;color:var(--ink);background:#fff;position:relative}
.abs{position:absolute}
.btn{display:flex;align-items:center;justify-content:center;border-radius:30px;font-weight:700;font-size:14px;text-transform:uppercase;color:#222;background:var(--yellow)}
.bar{width:70px;height:4px;background:var(--blue);border-radius:2px}

/* header */
.topbar{position:absolute;left:0;top:0;width:1200px;height:80px;border-top:3px solid var(--blue)}
.brand{left:110px;top:26px;font-size:22px;font-weight:700;color:var(--blue)}
.call{left:540px;top:18px;display:flex;align-items:center;gap:10px}
.call-icon{width:40px;height:40px;border:2px solid var(--blue);border-radius:50%;display:flex;align-items:center;justify-content:center}
.call small{font-size:13px;font-weight:700}
.call strong{font-size:21px;font-weight:700}
.schedule{left:894px;top:16px;width:178px;height:48px;font-size:14px}
.nav{left:0;top:80px;width:1200px;height:52px;background:var(--nav);display:flex;padding-left:115px}
.nav a{color:#fff;font-size:14px;text-decoration:none;padding:0 12px;display:flex;align-items:center}
.nav a.active{background:var(--yellow);color:#333}

/* hero */
.hero{left:0;top:132px;width:1200px;height:580px;background:linear-gradient(90deg,#8e8e8e 0%,#6d6d6d 45%,#555 70%,#3a3a3a 100%)}
.hero h1{left:110px;top:78px;width:700px;font-size:35px;line-height:44px;color:#fff;font-weight:700}
.hero p{left:110px;top:170px;width:650px;font-size:13px;line-height:26px;color:#fff}
.hero .btn{left:104px;top:258px;width:282px;height:48px}

.feature{top:489px;width:315px;height:366px;background:#fff;box-shadow:0 2px 10px rgba(0,0,0,.12);text-align:center}
.feature .ph{margin:5px;height:195px}
.feature h3{font-size:21px;line-height:30px;font-weight:700;margin-top:16px;padding:0 60px}
.feature p{font-size:13px;line-height:26px;color:var(--muted);margin-top:10px;padding:0 50px}
.feature .go{position:absolute;left:50%;bottom:-22px;transform:translateX(-50%);width:48px;height:48px;border-radius:50%;background:var(--blue);display:flex;align-items:center;justify-content:center}

/* about */
.about .bar{left:110px;top:972px}
.about h2{left:110px;top:995px;font-size:26px;font-weight:700}
.about p{left:111px;top:1033px;width:490px;font-size:14px;line-height:25.6px;color:#666}
.about .btn{left:112px;top:1236px;width:178px;height:48px}
.about .ph{left:657px;top:975px;width:433px;height:318px}

/* services */
.services{left:0;top:1388px;width:1200px;height:1114px;background:var(--grey-bg)}
.sec-title{width:1200px;text-align:center;font-size:26px;font-weight:700;text-transform:uppercase}
.center-bar{left:565px}
.svc{width:313px;height:363px}
.svc .tab{position:absolute;left:40px;top:-38px;width:233px;height:40px;background:#fff;text-align:center;font-size:17px;font-weight:700;line-height:42px}
.svc.on .tab{background:var(--blue);color:#fff}
.svc .card{position:absolute;left:0;top:0;width:313px;height:363px;background:#fff;text-align:center}
.svc .ph{margin:5px;height:193px}
.svc p{font-size:13px;line-height:26px;color:var(--muted);margin-top:18px;padding:0 32px}
.svc .btn{position:absolute;left:64px;bottom:-20px;width:185px;height:54px;background:var(--btn-grey);color:#fff;font-size:15px}
.svc.on .btn{background:var(--blue)}

/* reviews */
.reviews{left:0;top:2502px;width:1200px;height:405px;background:linear-gradient(90deg,#1a5ab0,#1d63bd 50%,#185aae);color:#fff;text-align:center}
.reviews .wbar{left:565px;top:48px;width:70px;height:3px;background:#fff}
.reviews h2{top:70px;width:1200px;font-size:26px;font-weight:700}
.reviews h4{top:128px;width:1200px;font-size:17px;font-weight:700}
.reviews p{left:200px;top:156px;width:800px;font-size:13px;line-height:26px;font-style:italic}
.reviews .btn{left:456px;top:290px;width:288px;height:54px}

/* process */
.process .bar{left:565px;top:2958px}
.step{top:3040px;width:230px;text-align:center}
.step h4{font-size:17px;font-weight:700;line-height:26px;height:52px}
.step .dot{width:116px;height:116px;border-radius:50%;background:var(--yellow);margin:0 auto;display:flex;align-items:center;justify-content:center}
.step p{font-size:13px;line-height:26px;color:var(--muted);margin-top:22px}

/* get started */
.start{left:0;top:3443px;width:1200px;height:322px;background:linear-gradient(90deg,#1957a8,#1e61b8)}
.start .wbar{left:565px;top:50px;width:70px;height:3px;background:#fff}
.start h2{top:70px;width:1200px;text-align:center;color:#fff;font-size:27px;font-weight:700}
.form{left:112px;top:3562px;width:978px;height:226px;background:#fff;box-shadow:0 2px 10px rgba(0,0,0,.15)}
.form label{position:absolute;left:48px;font-size:21px;font-weight:700;color:var(--blue)}
.field{position:absolute;width:219px;height:46px;background:var(--field);font-size:14px;color:#777;padding-left:12px;display:flex;align-items:center}
.field.sel::after{content:"";position:absolute;right:16px;top:21px;border:5px solid transparent;border-top-color:#555}
.form .btn{position:absolute;left:231px;top:160px;width:121px;height:40px;font-size:14px}

footer{left:108px;top:3822px;font-size:13px;color:#222}
</style>
</head>
<body>

<header class="topbar">
  <div class="abs brand">Keystone Flooring Florida</div>
  <div class="abs call">
    <div class="call-icon"><svg width="18" height="18" viewBox="0 0 24 24"><path fill="#1858a8" d="M6.6 10.8a15 15 0 006.6 6.6l2.2-2.2c.3-.3.7-.4 1-.2 1.1.4 2.3.6 3.6.6.6 0 1 .4 1 1V20c0 .6-.4 1-1 1A17 17 0 013 4c0-.6.4-1 1-1h3.5c.6 0 1 .4 1 1 0 1.3.2 2.5.6 3.6.1.3 0 .7-.2 1z"/></svg></div>
    <small>Call us Today :</small><strong>+1 555 014 2290</strong>
  </div>
  <div class="abs btn schedule">Schedule now</div>
</header>
<nav class="abs nav">
  <a class="active">Home</a><a>Tile Installation</a><a>Commercial Portfolio</a><a>Bathroom Tile Installation</a><a>Tile Backsplash Installation</a><a>Service Areas</a><a>Floor Removal</a>
</nav>

<section class="abs hero" role="img" aria-label="Modern grey interior with a curved white chair and a living room">
  <h1 class="abs">Experience premium flooring installation in Central Florida with Keystone Group</h1>
  <p class="abs">Are you tired of having your residential or commercial floors messed up by unprofessional services? Allow Keystone Group to change your floor installation and removal story today with our premium services, creativity, and personalized approach.</p>
  <div class="abs btn">Get your free estimate →</div>
</section>

<article class="abs feature" style="left:110px">
  <div class="ph" role="img" aria-label="Installer laying hexagon tiles on a wooden floor" style="background:linear-gradient(135deg,#e9d3bf,#b59a86)"></div>
  <h3>Minimal stress on your plate</h3>
  <p>Floor installation or removal can be stressful for both parties.</p>
  <div class="go"><svg width="20" height="20" viewBox="0 0 20 20"><circle cx="10" cy="10" r="9" fill="#fff"/><path d="M7 10h6M10 7l3 3-3 3" stroke="#1858a8" stroke-width="2" fill="none"/></svg></div>
</article>
<article class="abs feature" style="left:442px">
  <div class="ph" role="img" aria-label="Bright loft living room with tall windows" style="background:linear-gradient(135deg,#e2e2e0,#8a7766)"></div>
  <h3>A Floor worthy of your home</h3>
  <p>The quality and type of your floor are as important as its style and appeal.</p>
  <div class="go"><svg width="20" height="20" viewBox="0 0 20 20"><circle cx="10" cy="10" r="9" fill="#fff"/><path d="M7 10h6M10 7l3 3-3 3" stroke="#1858a8" stroke-width="2" fill="none"/></svg></div>
</article>
<article class="abs feature" style="left:775px">
  <div class="ph" role="img" aria-label="Open plan living room with staircase and white sofa" style="background:linear-gradient(135deg,#d7d7d7,#7a7a7a)"></div>
  <h3>Qualified and certified experts</h3>
  <p>After spending a lot to finally get that property of your dream, the</p>
  <div class="go"><svg width="20" height="20" viewBox="0 0 20 20"><circle cx="10" cy="10" r="9" fill="#fff"/><path d="M7 10h6M10 7l3 3-3 3" stroke="#1858a8" stroke-width="2" fill="none"/></svg></div>
</article>

<section class="about">
  <div class="abs bar"></div>
  <h2 class="abs">A RELIABLE PARTNER TO LEAN ON</h2>
  <p class="abs">Keystone Group comes with over 14 years of experience in floor installation. We are specialists when it comes to tile installation, hardwood installation, carpet installation, tile backsplash installation, vinyl installation, laminate floor installation, and floor removal. Over the years, we have come to position ourselves as the professional hands our customers need for all their installation and removal needs. With us, you can be assured of on-time performance, professional services, and prime craftsmanship.</p>
  <div class="abs btn">Learn more</div>
  <div class="abs ph" role="img" aria-label="Grey living room with sofa and shelving beside abstract grey shapes" style="background:linear-gradient(120deg,#e6e6e6,#9a9a9a 60%,#c2c2c2)"></div>
</section>

<section class="abs services">
  <div class="abs bar center-bar" style="top:58px"></div>
  <h2 class="abs sec-title" style="top:80px">Make your floors scream quality and beauty</h2>

  <div class="abs svc" style="left:110px;top:184px"><div class="tab">Tile installation</div><div class="card">
    <div class="ph" role="img" aria-label="Hands placing patterned cement tiles" style="background:linear-gradient(135deg,#9a9a9a,#5e7370)"></div>
    <p>Tile is one durable flooring material that, when placed well, leaves your home or property looking luxurious and inviting. Keystone Group is fitted</p>
    <div class="btn">Learn more</div></div></div>
  <div class="abs svc on" style="left:447px;top:184px"><div class="tab">Hardwood installation</div><div class="card">
    <div class="ph" role="img" aria-label="Worker hammering hardwood floor planks" style="background:linear-gradient(135deg,#2f5f9e,#a57f5a)"></div>
    <p>Are you looking for the best hardwood installers near you? You are at the right place. Keystone Group is an expert in all kinds of hardwood installation</p>
    <div class="btn">Learn more</div></div></div>
  <div class="abs svc" style="left:786px;top:184px"><div class="tab">Laminate installation</div><div class="card">
    <div class="ph" role="img" aria-label="Laminate boards being fitted with a tape measure" style="background:linear-gradient(135deg,#c9a883,#ece7df)"></div>
    <p>Adorning your floor with laminate material is often a great option to limit scratches, wear and tear, and improve floor durability. With a lot to</p>
    <div class="btn">Learn more</div></div></div>

  <div class="abs svc" style="left:110px;top:647px"><div class="tab">Carpet installation</div><div class="card">
    <div class="ph" role="img" aria-label="Installer rolling out teal carpet" style="background:linear-gradient(135deg,#6d6d6d,#8fb8b6)"></div>
    <p>Carpet installation is a good way to personalized the theme of your home, improve comfort, warmth, and a luxurious feel.</p>
    <div class="btn">Learn more</div></div></div>
  <div class="abs svc" style="left:447px;top:647px"><div class="tab">Vinyl installation</div><div class="card">
    <div class="ph" role="img" aria-label="Hands laying a dark vinyl plank" style="background:linear-gradient(135deg,#d6d6d6,#6b3f2c)"></div>
    <p>Vinyl flooring is a great option for families and businesses looking for a balance between the deep texture and feel of real wood tiles</p>
    <div class="btn">Learn more</div></div></div>
  <div class="abs svc" style="left:786px;top:647px"><div class="tab">Floor removal</div><div class="card">
    <div class="ph" role="img" aria-label="Scraper removing old floor tiles" style="background:linear-gradient(135deg,#7d8ea8,#c6ad88)"></div>
    <p>Removing your floor isn't an easy task, whether it is a carpet installation, hardwood, or concrete. It takes a lot of time and is</p>
    <div class="btn">Learn more</div></div></div>
</section>

<section class="abs reviews" role="img" aria-label="Blue tinted background of a worker fitting flooring">
  <div class="abs wbar"></div>
  <h2 class="abs">CUSTOMER REVIEWS</h2>
  <h4 class="abs">OUR PROMISE</h4>
  <p class="abs">Just like property remodeling or additions, installing a new floor isn't an easy job or something you just execute without lots of prep and planning. It is our goal to make the journey easier and convenient for you. We hope to materialize a floor installation process that starts off on a good leg and ends seamlessly, taking nothing from you. Hence, we do all we can from securing your fixed and unfixed assets from dust or damage to properly advising you on the right steps to take to create a timeless floor you and your loved ones can be proud of.</p>
  <div class="abs btn">Get your free estimate →</div>
</section>

<section class="process">
  <div class="abs bar"></div>
  <h2 class="abs sec-title" style="top:2980px">A simple, repeatable process</h2>
  <div class="abs step" style="left:98px"><h4>Schedule an appointment</h4>
    <div class="dot"><svg width="50" height="50" viewBox="0 0 50 50"><rect x="4" y="8" width="42" height="38" rx="4" fill="#222"/><rect x="8" y="18" width="34" height="24" fill="#ffd200"/><rect x="12" y="3" width="5" height="10" fill="#222"/><rect x="33" y="3" width="5" height="10" fill="#222"/><g fill="#222"><rect x="12" y="22" width="6" height="6"/><rect x="22" y="22" width="6" height="6"/><rect x="32" y="22" width="6" height="6"/><rect x="12" y="32" width="6" height="6"/><rect x="22" y="32" width="6" height="6"/><rect x="32" y="32" width="6" height="6"/></g></svg></div>
    <p>Fill out the form on our site or call us on our hotline to relay your needs and schedule a free site inspection. It is that simple!</p></div>
  <div class="abs step" style="left:355px"><h4>Your preferred floor material</h4>
    <div class="dot"><svg width="52" height="52" viewBox="0 0 52 52"><rect x="4" y="4" width="44" height="44" fill="none" stroke="#222" stroke-width="4"/><path d="M4 28L28 4M12 48L48 12M4 40L40 4M24 48L48 24" stroke="#222" stroke-width="5"/></svg></div>
    <p>Based on our findings on consultation and our inspection, we will help you figure out the right type of floor for your home or business space.</p></div>
  <div class="abs step" style="left:613px"><h4>Premium installation</h4>
    <div class="dot"><svg width="54" height="54" viewBox="0 0 54 54"><rect x="3" y="3" width="48" height="48" fill="#222"/><path d="M3 15L15 3M3 27L27 3M3 39L39 3M3 51L51 3M15 51L51 15M27 51L51 27M39 51L51 39M3 3L51 51M3 15L39 51M15 3L51 39" stroke="#ffd200" stroke-width="2"/></svg></div>
    <p>After the two stages are done, and you have approved the work date, our professionals for your floor will begin work on your property.</p></div>
  <div class="abs step" style="left:871px"><h4>A happy you!</h4>
    <div class="dot"><svg width="50" height="50" viewBox="0 0 50 50"><path d="M10 26l11 11 20-22" stroke="#222" stroke-width="7" fill="none" stroke-linecap="round" stroke-linejoin="round"/></svg></div>
    <p>With a quality job done, go ahead and enjoy your floors for years to come with minimal maintenance on your side!</p></div>
</section>

<section class="abs start" role="img" aria-label="Blue tinted background of flooring tools">
  <div class="abs wbar"></div>
  <h2 class="abs">GET STARTED NOW</h2>
</section>
<form class="abs form">
  <label style="top:38px">APPOINTMENT :</label>
  <div class="field sel" style="left:231px;top:28px">Type of appointment</div>
  <div class="field sel" style="left:458px;top:28px">Closest city</div>
  <div class="field sel" style="left:685px;top:28px">Date</div>
  <label style="top:98px">YOUR INFO :</label>
  <div class="field" style="left:231px;top:88px">Name..,</div>
  <div class="field" style="left:458px;top:88px">Contact info…</div>
  <div class="field" style="left:685px;top:88px">Address</div>
  <div class="btn">Submit</div>
</form>

<footer class="abs">© Copyrights 2020 Company name | All Rights Reserved</footer>
</body>
</html>
```